Deliver a professional and engaging investment propsal.

I am appealing to highend smart investors and need a high quality, engaging and formal presentation in PDF.
StowBin: https://www.stowbin.net/sh/qwmtr48kelvan2x/ZZTrPHmLe7WqsnBFjQ4kR8vYt?dl=0
Text for project is in Stowbin called New Proposal Final
Along with past much older attempts of this job.
Any additional ideas to enable a better outcome would be appreicated.

```html
<!DOCTYPE html>
<html lang="en">
<head>
<meta charset="utf-8">
<title>Ridgeline Business Park – Project Proposal</title>
<link href="https://fonts.googleapis.com/css2?family=Bebas+Neue&family=Open+Sans:wght@400;600;700&family=Roboto:wght@400;500&display=swap" rel="stylesheet">
<style>
:root{
  --backdrop:#8a8a8a;
  --paper:#ffffff;
  --ink:#2b2b2b;
  --header:#000000;
  --lime:#a6c31b;
  --olive:#8f9d1f;
  --olive-deep:#4d4f12;
  --gold:#e2c400;
  --sage:#b1c36a;
}
*{box-sizing:border-box;margin:0;padding:0}
html,body{width:1200px;height:1200px;overflow:hidden}
body{background:var(--backdrop);position:relative;font-family:"Open Sans",sans-serif;color:var(--ink)}
.page{position:absolute;width:370px;height:520px;background:var(--paper);overflow:hidden;box-shadow:6px 8px 14px rgba(0,0,0,.35)}
.page--cover{left:181px;top:58px}
.page--proposal{left:661px;top:58px}
.page--changes{left:181px;top:634px}
.page--location{left:661px;top:634px}

.brand{display:flex;align-items:center;gap:4px;font-family:"Open Sans",sans-serif;font-weight:600;color:#fff;letter-spacing:-.2px;white-space:nowrap}
.brand__mark{width:7px;height:7px;background:var(--lime)}
.page-header{position:absolute;left:0;top:0;width:100%;height:62px;background:var(--header)}
.page-header .brand{position:absolute;right:22px;top:26px;font-size:12px}

.cover-photo{position:absolute;left:0;top:0;width:370px;height:449px;
  background:linear-gradient(180deg,#1b4fa0 0%,#3f75b8 30%,#6f8db0 52%,#8a6a52 68%,#3a3c48 84%,#6c6a72 100%)}
.cover .brand{position:absolute;left:23px;top:50px;font-size:21px;font-weight:400}
.cover-panel{position:absolute;left:0;top:114px;width:195px;height:248px;background:rgba(143,157,31,.88)}
.cover-title{position:absolute;left:27px;top:28px;font-family:"Bebas Neue",sans-serif;font-weight:400;font-size:52px;line-height:.96;color:#fff;letter-spacing:.3px;white-space:nowrap}
.cover-band{position:absolute;left:0;top:139px;width:195px;height:54px;background:rgba(60,60,14,.88);padding:6px 0 0 26px;font-family:"Open Sans",sans-serif;font-weight:700;font-size:16.5px;line-height:1.3;color:#fff;white-space:nowrap}
.cover-sub{position:absolute;left:25px;top:208px;font-weight:700;font-size:10.5px;color:#fff;white-space:nowrap}
.cover-rule{position:absolute;left:34px;top:238px;width:118px;height:4px;background:rgba(70,70,40,.6)}
.cover-url{position:absolute;right:9px;top:489px;font-family:"Open Sans",sans-serif;font-size:8px;letter-spacing:1.4px;color:#111}

.tiles{position:absolute;left:22px;width:62px;height:68px}
.tile{position:absolute;width:29px;height:30px;background:linear-gradient(90deg,var(--sage),var(--gold))}
.tile--a{left:0;top:22px}
.tile--b{left:32px;top:0}
.tile--c{left:32px;top:38px}
.cover .tiles{top:437px}
.sheet .tiles{top:445px}
.accent-bar{position:absolute;right:0;width:175px;height:18px;background:linear-gradient(90deg,var(--sage) 0%,var(--sage) 45%,var(--gold) 100%)}
.cover .accent-bar{top:449px}
.sheet .accent-bar{top:485px}

.sheet-title{position:absolute;font-family:"Roboto",sans-serif;font-weight:500;color:var(--lime);line-height:1.1}
.body{position:absolute;font-family:"Open Sans",sans-serif;font-size:6.1px;line-height:1.38;color:#333}
.body p{margin-bottom:7px}
.body h3{font-family:"Roboto",sans-serif;font-weight:500;font-size:8.6px;color:var(--lime);margin:2px 0 7px}
.body ul{list-style:none}
.body li{position:relative;padding-left:6px;margin-bottom:8.4px}
.body li::before{content:"";position:absolute;left:0;top:2.2px;width:3px;height:3px;border-radius:50%;border:.8px solid #333}

.page--proposal .sheet-title{left:24px;top:76px;font-size:28px}
.page--proposal .body{left:26px;top:117px;width:324px}
.page--changes .sheet-title{left:19px;top:97px;font-size:22px}
.page--changes .body{left:24px;top:145px;width:324px}
.page--changes .body li{margin-bottom:10px}
.page--location .sheet-title{left:19px;top:68px;font-size:20px}
.page--location .body{left:21px;top:96px;width:326px;font-size:6.1px;line-height:1.4}
.page--location .body p{margin-bottom:8.5px}
</style>
</head>
<body>

<section class="page page--cover cover">
  <div class="cover-photo" role="img" aria-label="Photograph of a brick corner building on a town main street at dusk with light trails on the road"></div>
  <div class="brand"><span>CapitalBloom</span><span class="brand__mark"></span></div>
  <div class="cover-panel">
    <h1 class="cover-title">PROJECT<br>PROPOSAL</h1>
    <div class="cover-band">RIDGELINE<br>BUSINESS PARK</div>
    <div class="cover-sub">60 Acre Mixed-Use Devlopment</div>
    <div class="cover-rule"></div>
  </div>
  <div class="tiles"><span class="tile tile--a"></span><span class="tile tile--b"></span><span class="tile tile--c"></span></div>
  <div class="accent-bar"></div>
  <div class="cover-url">www.ridgeline-park.com</div>
</section>

<section class="page page--proposal sheet">
  <header class="page-header"><div class="brand"><span>CapitalBloom</span><span class="brand__mark"></span></div></header>
  <h2 class="sheet-title">Proposal</h2>
  <div class="body">
    <p>We have an incredible property, Ridgeline Business Park, located at 1870 Prairie Route 12 McKenzie County, Watford City, North Dakota 58854 USA which we have fully funded with cash and now need a joint venture partner, buyer or lender to get this project to completion and producing a substantial profit we all can share.</p>
    <p>Our property is located on the best oil reserves in the world in North Dakota USA, with more oil than any other county in the Bakken Basin and with the lowest recoverable costs of $24 a barrel.</p>
    <p>We own the property and need a partner to develop the site and bring to the market at half the cost of competing business parks in the area.</p>
    <h3>Participation Options</h3>
    <ul>
      <li>A joint venture partner would support all the costs developing the property without the upfront costs of the property purchase.</li>
      <li>All sales would be split to ensure both parties are paid out in such a way that both are paid out in full at the same time then a 50/50 profit share split on all remaining sales.</li>
      <li>Contract drawn up protecting and supporting both parties on agreed terms4</li>
      <li>As a potential joint venture partner, I would cover the full property (57.7 acres) cost as mentioned of $124,784 per acre (57.7 acres). ($7,200,000)</li>
      <li>Joint venture partner to supply the development costs estimated to be around $65,000 an acre estimated pending tender selection and additional refundable security bonds held with the Watford City on development works.</li>
      <li>Development costs could be in up to three stages to lower outlay and limit exposure if so desired, however it will take longer to complete and bring to market.</li>
      <li>A buyer can be fully supported by myself to oversee the full project and outcomes and support the budgets of construction and sales to get the highest returns for a small fee.</li>
      <li>To purchase the property, you would need to contact me directly and I can introduce you to our realtor who will discount his commission from 6% to 5% which is a significant saving.</li>
      <li>Financing on excellent terms allowing 12 to 18 months for income streams and could be linked to a joint venture option / profit share.</li>
    </ul>
  </div>
  <div class="tiles"><span class="tile tile--a"></span><span class="tile tile--b"></span><span class="tile tile--c"></span></div>
  <div class="accent-bar"></div>
</section>

<section class="page page--changes sheet">
  <header class="page-header"><div class="brand"><span>CapitalBloom</span><span class="brand__mark"></span></div></header>
  <h2 class="sheet-title">Major Site Changes</h2>
  <div class="body">
    <ul>
      <li>We purchased the property in in 2013 for cash and without any additional debt, at the time we had highway 85 frontage just outside Watford City limits South of town with a zoning of agricultural within McKenzie County.</li>
      <li>2014 site zoning changed allowing a commercial zoning.</li>
      <li>Flag Hotel site purchased 2014 now with the option to purchase the franchise license and build the hotel ourselves.</li>
      <li>In 2016 we were added into City Limits which was a massive improvement to our site now taking advantage of confirmed city water and sewer was a great outcome.</li>
      <li>In 2016 the new bypass opened intersecting our highway frontage just 100 yards away which brings all the traffic in the Bakken right past our site which was a massive win for this project.</li>
      <li>Same commercial property listed across the road at $750,000 per acre retail at Larkfield Commons and other business parks average listings $550,00 per acre.</li>
      <li>In late 2017 we applied for full site development application and were approved in mid-2018 which again was a significant improvement to the project.</li>
      <li>May 2018 Full site infrastructure development approval which includes all roads and city services, this will trigger interest in the site from passing traffic and with a great marketing campaign will surely start sales coming in quickly once we break ground and start work.</li>
      <li>We also can buy the franchise license of the Summit Lodge hotel for additional income potential if desired.</li>
    </ul>
  </div>
  <div class="tiles"><span class="tile tile--a"></span><span class="tile tile--b"></span><span class="tile tile--c"></span></div>
  <div class="accent-bar"></div>
</section>

<section class="page page--location sheet">
  <header class="page-header"><div class="brand"><span>CapitalBloom</span><span class="brand__mark"></span></div></header>
  <h2 class="sheet-title">Location</h2>
  <div class="body">
    <p>Our property is ideally located in Watford City, United States of America, despite its humble beginnings, has suddenly found itself at the epicentre of the Bakken oil boom Located in Western North Dakota the city has seen workers flood into the area over recent years to fill positions to support the growth.</p>
    <p>McKenzie County where Watford City is located has more recoverable oil and gas at the lowest recoverable cost per barrel at $24, making it most affordable anywhere in the Bakken basin, centrally located and very desirable area to establish a business and company headquarters.</p>
    <p>Watford City is the crossroads whereby around 20,000 vehicles pass by our site each day travelling locally and between Williston where boom started and Dickinson an established town with relevant established support for business and infrastructure. Our project has highway frontage and is 100 yards away from the bypass intersection making it the best location in McKenzie County for this type of project.</p>
    <p>With billions invested into infrastructure in the past 5 years in and around Bakken Shale Oil Basin our project has become the beneficiary of a major new Watford City bypass which intersects highway 85 just 100 yards south of our project, putting us on one of the busiest intersections in the Bakken. With this rapid growth we were included into the Watford City limits providing additional benefits to the overall success for our development including all city services.</p>
    <p>Demand stems from the ongoing boom in oil and gas drilling in the area which is still in its infancy stages of life, North Dakota oil play and is expected to continue to grow well past 2050 based on obtainable reserves beneath the ground.</p>
    <p>Additional location growth:</p>
    <p>Northfield Energy 150 million-dollar Watford City investment 2018</p>
    <p>North Dakota is the nation’s second-biggest oil producer</p>
    <p>McKenzie County Investment. Development</p>
    <p>Within the 100 yards of Ridgeline Business park, directly across the road commercial land is currently listed at of $750,000 an acre at Larkfield Commons and many more locations up to $650,000 per acre. With an advantage over other sites in terms of a better location and much lower purchase and development costs the numbers don’t lie, and we need to have pad ready to build lots to offer the market.</p>
    <p>Bakken traffic, North, South, East and West will have to travel right by our site making it the second busiest intersection in the Bakken area, giving us the best exposure to sell, promote and grow, this site can and will be the location for new business and growth, we need to develop the site now to move forward.</p>
    <p>With our obvious high exposure to potential buyers through the passing traffic and lower entry price point there is no doubt Ridgeline Town Center will become the place where business will want to build alongside a quality business like the Summit Lodge Plus Extended Stay Hotel.</p>
  </div>
</section>

</body>
</html>
```